Broschüre für Energieberater
Zielgruppe
Unternehmen die zu den KMU´s gehören (kleine und mittlere Unternehmen) haben die Möglichkeit eine Energieberatung über die ZEKV fördern zu lassen. Diese Beratung wird durch unsere Ingenieure durchgeführt und ist für den Kunden völlig kostenneutral. Zum einen erhält er eine 80% Förderung von der ZEKV (Zentralstelle für Kostenausgleich und Versorgung) die restlichen 20% erhält der Kunde von uns als Gutschrift. Wir finanzieren uns somit nur über die Fördergelder des Bundes. Die Vorteile des Kunden sind: Verringerung von Steuern, Einsparung von mindestens 10% an Energie ohne zusätzliche Kosten und somit weniger C0² Ausstoss, was wiederum allen zugute kommt. Somit ein hohes Maß an Umweltbewusstsein! Alle Investitionen die für die Einsparung von Energie von Vorteil sind, werden vom Bund mit bis zu 200.000 Euro gefördert. Voraussetzung eine durchgeführte ZEKV Energieberatung. Somit eine win/win Situation für alle Beteiligten.
Aufgabenstellung
Das Design kann - muss - nicht an unsere Webseite : www.wattlinde-beratung.de angelehnt sein.

```html
<!DOCTYPE html>
<html lang="de">
<head>
<meta charset="utf-8">
<title>Wattlinde – Energie Effizienz Broschüre</title>
<link href="https://fonts.googleapis.com/css2?family=Hind:wght@300;400;600&family=PT+Sans+Narrow&display=swap" rel="stylesheet">
<style>
  :root {
    --bg: #e9e9e7;
    --paper: #f6f6f6;
    --blue: #3b7ec0;
    --blue-text: #3f86c6;
    --grey-tile: #9e9e9e;
    --grey-page: #c6c6c6;
    --grey-logo: #a3a3a3;
    --ink: #3a3a3a;
    --ink-soft: #6a6a6a;
    --white: #ffffff;
  }
  * { box-sizing: border-box; margin: 0; padding: 0; }
  html, body { width: 1200px; height: 900px; overflow: hidden; }
  body { background: var(--bg); font-family: "Hind", sans-serif; position: relative; }

  /* Cover */
  .cover { position: absolute; left: 39px; top: 203px; width: 369px; height: 517px; background: var(--paper); box-shadow: 0 4px 14px rgba(0,0,0,.12); }
  .cover__brand { position: absolute; left: 38px; top: 34px; font-family: "Hind", sans-serif; font-weight: 600; font-size: 36px; color: var(--grey-logo); letter-spacing: -0.5px; }
  .cover__photo { position: absolute; left: 0; top: 112px; width: 369px; height: 345px; background: radial-gradient(circle at 50% 55%, #c9893a 0%, #5a4a35 18%, #1f3340 45%, #142531 100%); }
  .cover__title { position: absolute; right: 36px; bottom: 22px; font-family: "PT Sans Narrow", sans-serif; font-size: 25px; color: var(--blue-text); }

  /* Spread */
  .spread { position: absolute; left: 439px; top: 205px; width: 717px; height: 517px; box-shadow: 0 4px 14px rgba(0,0,0,.12); }
  .page { position: absolute; top: 0; height: 517px; background: var(--paper); }
  .page--left { left: 0; width: 359px; }
  .page--right { left: 359px; width: 358px; }
  .page--left .page__band { position: absolute; left: 0; right: 0; top: 203px; bottom: 0; background: linear-gradient(180deg, var(--grey-page), #d2d2d2); }
  .page__photo { position: absolute; left: 37px; top: 33px; width: 288px; height: 220px; background: radial-gradient(ellipse at 50% 50%, #9fb1b8 0%, #cfcfcf 40%, #e2e2e2 75%, #bdbdbd 100%); }
  .page__headline { position: absolute; left: 38px; top: 302px; font-weight: 300; font-size: 22px; line-height: 22px; color: var(--blue-text); }
  .page__copy { position: absolute; left: 111px; top: 380px; width: 210px; font-family: "PT Sans Narrow", sans-serif; font-size: 6.2px; line-height: 9.2px; color: var(--ink-soft); }

  .intro { position: absolute; left: 34px; top: 30px; width: 245px; font-weight: 300; font-size: 10.4px; line-height: 13.6px; color: var(--ink); }

  .feature { position: absolute; display: flex; height: 84px; }
  .feature__icon { width: 74px; height: 100%; background: var(--grey-tile); display: flex; align-items: center; justify-content: center; }
  .feature__body { background: var(--blue); color: var(--white); padding: 10px 8px 0 9px; }
  .feature__title { font-weight: 400; font-size: 9.6px; line-height: 11px; margin-bottom: 3px; }
  .feature__text { font-weight: 300; font-size: 6.6px; line-height: 8.6px; }

  .feature--costs { left: 34px; top: 107px; }
  .feature--costs .feature__body { width: 214px; }
  .feature--funding { left: 0; top: 202px; }
  .feature--funding .feature__body { width: 248px; padding-left: 34px; }
  .feature--savings { left: 34px; top: 295px; }
  .feature--savings .feature__body { width: 250px; }
  .feature--experts { left: 34px; top: 387px; }
  .feature--experts .feature__body { width: 214px; }

  .euro { font-family: "Hind", sans-serif; font-weight: 600; font-size: 52px; color: #efefef; line-height: 1; margin-top: 8px; }
</style>
</head>
<body>

<section class="cover">
  <div class="cover__brand">Wattlinde</div>
  <div class="cover__photo" role="img" aria-label="Foto einer leuchtenden Glühbirne mit Glühfaden vor dunklem Hintergrund"></div>
  <h1 class="cover__title">Energie Effizienz</h1>
</section>

<section class="spread">
  <article class="page page--left">
    <div class="page__band"></div>
    <div class="page__photo" role="img" aria-label="Foto von zwei offenen Händen mit Euro-Geldscheinen"></div>
    <h2 class="page__headline">Energie sparen<br>heißt Geld sparen!</h2>
    <p class="page__copy">Eine effizientere Nutzung der Energie zu erreichen, bedeutet nicht gleichzeitig immer größere Investitionen tätigen zu müssen. Bereits durch die Optimierung bestehender Betriebsprozesse können erhebliche Energiekostenreduzierungen erreicht werden. Dies ist für Sie somit völlig kostenneutral! Durch eine geförderte Energieberatung erhalten Sie bei minimalem eigenen Aufwand einen maximalen Überblick über den aktuellen Energieverbrauch in Ihrem Unternehmen, sowie konkrete Vorschläge und betriebswirtschaftliche Berechnungen für Maßnahmen zur Optimierung Ihres Energieverbrauchs!</p>
  </article>

  <article class="page page--right">
    <p class="intro">Erhalten Sie jetzt Ihre staatlich geförderte Energieberatung, lassen Sie sich von Anfang an von Experten begleiten und sparen Sie ab sofort Energie und damit bares Geld!</p>

    <div class="feature feature--costs">
      <div class="feature__icon"><span class="euro">€</span></div>
      <div class="feature__body">
        <h3 class="feature__title">Keine versteckten Kosten!</h3>
        <p class="feature__text">Deutschland ist beim Erreichen seiner Klimaziele nicht auf Kurs und will deshalb mit dem Fördern von Energieberatungen mittelständische deutsche Unternehmen motivieren, energiesparende Maßnahmen zu treffen. Die darin empfohlenen Umsetzungen sind freiwillig. Zu keinem Zeitpunkt entstehen Ihnen versteckte Kosten!</p>
      </div>
    </div>

    <div class="feature feature--funding">
      <div class="feature__body">
        <h3 class="feature__title">Staatliche Fördermittel sichern!</h3>
        <p class="feature__text">Die Fördermittel sind aktuell gesichert, dies kann der Gesetzgeber jedoch jederzeit ändern. Fördermittel sollten daher genutzt werden, solange sie zur Verfügung stehen. Die Fördermittel werden von der Zentralstelle für Kostenausgleich und Versorgung bereitgestellt.</p>
      </div>
      <div class="feature__icon">
        <svg width="46" height="52" viewBox="0 0 46 52" aria-hidden="true">
          <rect x="2" y="8" width="42" height="42" rx="4" fill="#efefef"/>
          <rect x="2" y="18" width="42" height="3" fill="#9e9e9e"/>
          <rect x="10" y="2" width="5" height="12" rx="2" fill="#efefef"/>
          <rect x="31" y="2" width="5" height="12" rx="2" fill="#efefef"/>
          <g fill="#9e9e9e">
            <rect x="8" y="26" width="7" height="6"/><rect x="19.5" y="26" width="7" height="6"/><rect x="31" y="26" width="7" height="6"/>
            <rect x="8" y="37" width="7" height="6"/><rect x="19.5" y="37" width="7" height="6"/><rect x="31" y="37" width="7" height="6"/>
          </g>
        </svg>
      </div>
    </div>

    <div class="feature feature--savings">
      <div class="feature__icon">
        <svg width="38" height="54" viewBox="0 0 38 54" aria-hidden="true">
          <path d="M19 2C9 2 2 9.5 2 19c0 7 4 11 7 15 1.5 2 2 4 2 6h16c0-2 .5-4 2-6 3-4 7-8 7-15C36 9.5 29 2 19 2z" fill="#efefef"/>
          <path d="M10 19c0-5 4-9 9-9" stroke="#9e9e9e" stroke-width="3" fill="none" stroke-linecap="round"/>
          <rect x="11" y="43" width="16" height="4" rx="1" fill="#efefef"/>
          <rect x="13" y="48" width="12" height="4" rx="2" fill="#efefef"/>
        </svg>
      </div>
      <div class="feature__body">
        <h3 class="feature__title">Bis zu 25% Energie &amp; Kosten einsparen</h3>
        <p class="feature__text">Viele Unternehmer wurden bisher noch nicht ausreichend über ihren Energiehaushalt aufgeklärt. Ein auf Energieberatung spezialisierter Ingenieur erkennt schnell, an welchen Ecken mit wenig Aufwand viel Energie gespart werden kann. So wird langfristig nicht nur die Umwelt, sondern auch der eigene Geldbeutel geschont.</p>
      </div>
    </div>

    <div class="feature feature--experts">
      <div class="feature__body">
        <h3 class="feature__title">Experten gesicherte Durchführung</h3>
        <p class="feature__text">Wattlinde kann dank seiner langen Erfahrung in der Energiebranche eine problemlose Anmeldung garantieren. Alle Formulare müssen optimal ausgefüllt sein, um die Chancen auf eine maximale Förderung zu gewährleisten. Wenn die Zusage zur Förderung eintrifft, wird Wattlinde einen vom Staat zertifizierten Ingenieur zur Energieberatung vorbei schicken.</p>
      </div>
      <div class="feature__icon">
        <svg width="52" height="48" viewBox="0 0 52 48" aria-hidden="true">
          <circle cx="18" cy="13" r="11" fill="#efefef"/>
          <path d="M0 46c0-11 8-18 18-18s18 7 18 18z" fill="#efefef"/>
          <path d="M30 24l7 7 13-14" stroke="#efefef" stroke-width="5" fill="none" stroke-linecap="round" stroke-linejoin="round"/>
        </svg>
      </div>
    </div>
  </article>
</section>

</body>
</html>
```